Monument sign* - Law Firm

*I am installing a monument sign that has LED, as well as backlit elements. I am seeking help in designing the backlit portion of the sign. The Backlit sign will be 12’ x 4’.

We are looking for a classic, yet eye-catching sign to help new and current clients find our firm as well as bring in future clients. One of our goals is that people who drive by on a regular basis remember our sign (and us) for any future legal need.

Target Market(s)

Current and future clientele

Industry/Entity Type

Law Firm

Font styles to use
Serif
Sans Serif

Colors
b1b1b1
333333

Requirements
Must have
• Business name: Hargrove Law Firm, Inc.
• Website: www.hargrovelawfirm-example.com
• Telephone: (555)214-3679
• Our firm's logo
Nice to have
• Color preference is black, taupe, and white. A photo for reference of the office coloring is uploaded.
• We currently have an established logo which our firm has been using for more than 10 years. Our logo has been used in advertising, commercials, letterhead, and on-site. We are looking to transition from brown/rust/cream to the black/taupe/white color scheme.
Should not have
• Cheesy slogans; character designs; directions; additional symbols outside of the firm's logo.

```html
<!DOCTYPE html>
<html lang="en">
<head>
<meta charset="utf-8">
<title>Hargrove Law Firm, Inc. — Backlit Sign</title>
<link rel="stylesheet" href="https://fonts.googleapis.com/css2?family=Playfair+Display:wght@700;900&family=Montserrat:wght@700&display=swap">
<style>
  :root {
    --canvas-bg: #e4e4e2;
    --sign-face: #ffffff;
    --ink: #1c1c1c;
    --band: #222222;
    --band-text: #ffffff;
    --taupe: #8c8379;
  }
  * { margin: 0; padding: 0; box-sizing: border-box; }
  html, body { width: 894px; height: 1200px; overflow: hidden; }
  body {
    background: var(--canvas-bg);
    display: flex;
    align-items: center;
    justify-content: center;
  }
  .sign {
    width: 840px;
    height: 280px;
    background: var(--sign-face);
    display: flex;
    flex-direction: column;
    box-shadow: 0 2px 6px rgba(0,0,0,0.15);
  }
  .sign-face {
    flex: 1;
    display: flex;
    align-items: center;
    padding: 0 30px 0 22px;
  }
  .brand-square {
    width: 150px;
    height: 150px;
    background: var(--taupe);
    flex-shrink: 0;
  }
  .firm-name {
    margin-left: auto;
    color: var(--ink);
    font-family: "Playfair Display", serif;
    font-weight: 700;
    line-height: 0.95;
  }
  .firm-name-main {
    display: block;
    font-weight: 900;
    font-size: 84px;
    letter-spacing: 1px;
  }
  .firm-name-sub {
    display: block;
    font-size: 40px;
    margin-left: 4px;
    letter-spacing: 1px;
  }
  .firm-name-sub .caps-small { font-size: 32px; }
  .contact-band {
    height: 56px;
    background: var(--band);
    color: var(--band-text);
    font-family: "Montserrat", sans-serif;
    font-weight: 700;
    font-size: 19px;
    letter-spacing: 1.5px;
    display: flex;
    align-items: center;
    justify-content: center;
    gap: 14px;
  }
  .contact-divider {
    width: 2px;
    height: 22px;
    background: var(--band-text);
  }
</style>
</head>
<body>
  <section class="sign" aria-label="Hargrove Law Firm backlit sign">
    <div class="sign-face">
      <div class="brand-square" aria-hidden="true"></div>
      <h1 class="firm-name">
        <span class="firm-name-main">HARGROVE</span>
        <span class="firm-name-sub">L<span class="caps-small">AW</span> F<span class="caps-small">IRM</span>, Inc.</span>
      </h1>
    </div>
    <div class="contact-band">
      <span class="contact-web">WWW.HARGROVELAWFIRM-EXAMPLE.COM</span>
      <span class="contact-divider" aria-hidden="true"></span>
      <span class="contact-phone">(555)214-3679</span>
    </div>
  </section>
</body>
</html>
```